Home Remodeling company needs a business card design

we need a business card design for home remodeling company in hamilton county, indiana USA. we offers a wide range of construction services including whole house renovations, Design and Build Basements and Kitchen and Bathroom Remodeling . we would like to see designs for both site of business card that use the same color of the company logo and also including all information below :
1- Samir Daoudi CEO / General Contractor
2- all company contacts Telephone numbers ( 1-888-TOVAL-42 ) ( 317-555-0192) email address ( info@tovalhome.example) website ( www.tovalhome.example ) and social media logos (Facebook- twitter- google plus )
3- company logo
4- licensed . insured . bonded

```html
<!DOCTYPE html>
<html lang="en">
<head>
<meta charset="utf-8">
<title>Toval Home Remodeling – Business Card</title>
<link rel="stylesheet" href="https://fonts.googleapis.com/css2?family=Roboto:wght@500;700;900&display=swap">
<style>
  :root {
    --ink: #2f2c2c;
    --red: #d43a46;
    --red-deep: #c62d38;
    --tab: #efefef;
    --paper-light: #f4f4f4;
    --paper-mid: #e2e2e2;
    --white: #ffffff;
  }
  html, body {
    margin: 0;
    padding: 0;
    width: 1200px;
    height: 735px;
    overflow: hidden;
    background: #ffffff;
  }
  .card {
    position: relative;
    width: 1200px;
    height: 735px;
    overflow: hidden;
    font-family: "Roboto", Arial, sans-serif;
    color: var(--ink);
    background: linear-gradient(180deg, var(--paper-light) 0%, var(--paper-mid) 50%, var(--paper-light) 100%);
  }
  .company-name {
    position: absolute;
    left: 59px;
    top: 84px;
    margin: 0;
    font-size: 44px;
    font-weight: 700;
    line-height: 1;
    color: var(--ink);
    white-space: nowrap;
  }
  .person {
    position: absolute;
    left: 56px;
    top: 230px;
    width: 489px;
  }
  .person-name {
    margin: 0;
    padding: 0 0 8px 15px;
    font-size: 56px;
    font-weight: 700;
    line-height: 1;
    border-bottom: 2px solid var(--ink);
    white-space: nowrap;
  }
  .person-name .surname { color: var(--red); }
  .person-role {
    margin: 8px 0 0 23px;
    font-size: 33px;
    font-weight: 500;
    line-height: 1;
    white-space: nowrap;
  }
  .phones {
    position: absolute;
    right: 52px;
    top: 251px;
    text-align: right;
    font-size: 35px;
    font-weight: 700;
    line-height: 38px;
  }
  .phone-bar {
    position: absolute;
    right: 0;
    width: 31px;
  }
  .phone-bar.dark { top: 240px; height: 47px; background: var(--ink); }
  .phone-bar.red  { top: 287px; height: 47px; background: var(--red); }
  .band {
    position: absolute;
    left: 0;
    top: 446px;
    width: 1200px;
    height: 289px;
    background: var(--red-deep);
  }
  .band svg { position: absolute; left: 0; top: 0; }
  .credential {
    position: absolute;
    top: 446px;
    height: 64px;
    display: flex;
    align-items: center;
    justify-content: center;
    font-size: 41px;
    font-weight: 700;
    color: var(--ink);
  }
  .credential.licensed { left: 200px; width: 232px; }
  .credential.insured  { left: 484px; width: 230px; }
  .credential.bonded   { left: 766px; width: 228px; }
  .social {
    position: absolute;
    top: 624px;
    left: 0;
    height: 48px;
    color: var(--white);
    font-size: 25px;
    font-weight: 700;
  }
  .social-item {
    position: absolute;
    top: 0;
    height: 48px;
    display: flex;
    align-items: center;
    gap: 12px;
    white-space: nowrap;
  }
  .social-square {
    width: 44px;
    height: 44px;
    background: var(--white);
    opacity: 0.9;
  }
  .social-item.one   { left: 262px; }
  .social-item.two   { left: 494px; }
  .social-item.three { left: 741px; }
  .contact-line {
    position: absolute;
    top: 689px;
    font-size: 25px;
    font-weight: 700;
    color: var(--white);
    white-space: nowrap;
  }
  .contact-line.web   { left: 307px; }
  .contact-line.email { left: 629px; }
</style>
</head>
<body>
<main class="card">
  <p class="company-name">Toval Home Remodeling</p>

  <div class="person">
    <h1 class="person-name">SAMIR <span class="surname">DAOUDI</span></h1>
    <p class="person-role">CEO / General Contractor</p>
  </div>

  <div class="phones">
    <div class="phone">317-555-0192</div>
    <div class="phone">1-888-TOVAL-42</div>
  </div>
  <span class="phone-bar dark"></span>
  <span class="phone-bar red"></span>

  <div class="band">
    <svg width="1200" height="64" viewBox="0 0 1200 64" aria-hidden="true">
      <rect x="0" y="0" width="1200" height="64" fill="var(--red)"/>
      <polygon points="206,0 440,0 426,64 194,64" fill="var(--tab)"/>
      <polygon points="440,0 452,0 438,64 426,64" fill="var(--ink)"/>
      <polygon points="488,0 722,0 708,64 478,64" fill="var(--tab)"/>
      <polygon points="722,0 734,0 720,64 708,64" fill="var(--ink)"/>
      <polygon points="774,0 1002,0 988,64 759,64" fill="var(--tab)"/>
      <polygon points="1002,0 1014,0 1000,64 988,64" fill="var(--ink)"/>
    </svg>
  </div>
  <div class="credential licensed">•licensed</div>
  <div class="credential insured">• insured</div>
  <div class="credential bonded">•bonded</div>

  <div class="social">
    <div class="social-item one"><span class="social-square"></span>@tovalhome</div>
    <div class="social-item two"><span class="social-square"></span>&nbsp;&nbsp;tovalhome</div>
    <div class="social-item three"><span class="social-square"></span>@tovalhome</div>
  </div>
  <div class="contact-line web">www.tovalhome.example</div>
  <div class="contact-line email">info@tovalhome.example</div>
</main>
</body>
</html>
```